Business card to be used as a flyer

This business card should do the trick of a full scale flyer , so basicaly from the business card itself we only keep the size and remove the clasical name , position , company name (etc).
This business cards should be , like said above, used as promo tool, being gived to different girls . So base one : the design is girls oriented.
Colors : black background . We will use gold (color) folio for the text.
Attached you have our logo, but this should not be a proiminent part of the design . You can use only the cat head instead.
Target Market(s)
Girls / Women
Contact Information for Business Card
> black background , gold / folio text and elements
> cat head from the logo in a creative way do be displayed
> proieminent text "your path to success starts here"
> contact details phone and website .
www.velvadrome.ro (website) and 0741263519 (phone)
Font styles to use
Colors
Designer to choose only greyscale colors for use in the design.
Look and feel

```html
<!DOCTYPE html>
<html lang="en">
<head>
<meta charset="utf-8">
<title>Velvadrome studio – business card flyer</title>
<link rel="stylesheet" href="https://fonts.googleapis.com/css2?family=Montserrat:wght@800&family=Noto+Serif&family=Great+Vibes&display=swap">
<style>
  :root {
    --backdrop: #2a2c30;
    --card-white: #ffffff;
    --card-black: #0b0b0b;
    --band-black: #111111;
    --gold: #d9b64a;
    --gold-deep: #a8862a;
    --ink: #141414;
  }
  * { margin: 0; padding: 0; box-sizing: border-box; }
  html, body {
    width: 1200px; height: 900px; overflow: hidden;
    background: var(--backdrop);
  }
  .canvas {
    position: relative; width: 1200px; height: 900px;
    display: flex; flex-direction: column; align-items: center; justify-content: center;
    gap: 50px;
  }
  .card {
    position: relative; width: 640px; height: 360px;
    overflow: hidden; border-radius: 4px;
    box-shadow: 0 14px 30px rgba(0,0,0,.45);
  }

  /* Front face */
  .card-front { background: var(--card-white); }
  .brand {
    position: absolute; top: 36px; left: 0; right: 0;
    text-align: center; color: var(--ink);
    font-family: "Montserrat", sans-serif; font-weight: 800;
  }
  .brand-name { font-size: 34px; letter-spacing: 2px; line-height: 1; }
  .brand-sub { font-size: 15px; letter-spacing: 1px; margin-top: 4px; }
  .contact-band {
    position: absolute; left: 0; right: 0; top: 124px; height: 84px;
    background: var(--band-black);
    border-bottom: 4px solid var(--gold);
    display: flex; align-items: center; justify-content: center; gap: 54px;
    font-family: "Noto Serif", serif; font-size: 21px; color: var(--gold);
  }
  .contact-item { display: flex; align-items: center; gap: 10px; white-space: nowrap; }
  .contact-item svg { width: 20px; height: 20px; fill: var(--gold); }
  .tagline {
    position: absolute; left: 0; right: 0; top: 208px; bottom: 0;
    display: flex; align-items: center; justify-content: center;
    color: var(--gold); white-space: nowrap;
    font-family: "Great Vibes", cursive; font-size: 46px; line-height: 1;
  }

  /* Back face */
  .card-back {
    background:
      repeating-linear-gradient(115deg, rgba(255,255,255,.025) 0 40px, rgba(0,0,0,0) 40px 90px),
      var(--card-black);
  }
  .cat-emblem {
    position: absolute; left: 90px; top: 40px; width: 260px; height: 200px;
    border-radius: 40% 50% 45% 30%;
    background: radial-gradient(circle at 45% 40%, var(--gold) 0%, var(--gold-deep) 60%, rgba(168,134,42,0) 100%);
    opacity: .85;
  }
</style>
</head>
<body>
  <main class="canvas">
    <section class="card card-front" aria-label="Card front">
      <div class="brand">
        <div class="brand-name">VELVADROME</div>
        <div class="brand-sub">studio</div>
      </div>
      <div class="contact-band">
        <span class="contact-item">
          <svg viewBox="0 0 24 24" aria-hidden="true"><path d="M6.6 10.8a15.1 15.1 0 0 0 6.6 6.6l2.2-2.2c.3-.3.7-.4 1-.2 1.1.4 2.3.6 3.6.6.6 0 1 .4 1 1V20c0 .6-.4 1-1 1A17 17 0 0 1 3 4c0-.6.4-1 1-1h3.5c.6 0 1 .4 1 1 0 1.3.2 2.5.6 3.6.1.3 0 .7-.2 1z"/></svg>
          0741263519
        </span>
        <span class="contact-item">
          <svg viewBox="0 0 24 24" aria-hidden="true"><path d="M12 2a10 10 0 1 0 0 20 10 10 0 0 0 0-20zm6.9 6h-2.9a15.6 15.6 0 0 0-1.4-3.6A8 8 0 0 1 18.9 8zM12 4c.8 1.2 1.5 2.5 1.9 4h-3.8c.4-1.5 1.1-2.8 1.900-4zM4.3 14a8 8 0 0 1 0-4h3.4a16 16 0 0 0 0 4zm.8 2h2.9c.3 1.3.8 2.5 1.4 3.6A8 8 0 0 1 5.1 16zM8 8H5.1a8 8 0 0 1 4.3-3.6C8.8 5.5 8.3 6.7 8 8zm4 12c-.8-1.2-1.5-2.5-1.9-4h3.8c-.4 1.5-1.1 2.8-1.9 4zm2.3-6H9.7a14.6 14.6 0 0 1 0-4h4.6a14.6 14.6 0 0 1 0 4zm.3 5.6c.6-1.1 1.1-2.3 1.4-3.6h2.9a8 8 0 0 1-4.3 3.6zm1.7-5.6a16 16 0 0 0 0-4h3.4a8 8 0 0 1 0 4z"/></svg>
          www.velvadrome.ro
        </span>
      </div>
      <p class="tagline">Your Path to Success Starts Here</p>
    </section>

    <section class="card card-back" aria-label="Card back">
      <div class="cat-emblem" role="img" aria-label="Gold line illustration of a cat head and neck"></div>
    </section>
  </main>
</body>
</html>
```